Technology Solutions Provider

Let’s design a business card that will be as simple and bold at the same time. Name, email address, website & phone number.

Target Market(s)

Small to Medium Size Business

Industry/Entity Type

It Professional

Contact Information for Business Card

Name, email, website, phone numbers

Font styles to use
Sans Serif

Colors
ec1f27
f04a50
dddddd
919191
000000
ffffff

Requirements
Must have
• Clean simple look using my existing logo. I just need to the basic contact information on this card.
Nice to have
• Im considering the square size card versus the standard size business card.
Should not have
• No Mailing Address, no list of services.

```html
<!DOCTYPE html>
<html lang="en">
<head>
<meta charset="utf-8">
<title>Veltra Systems – Business Card</title>
<link rel="stylesheet" href="https://fonts.googleapis.com/css2?family=Montserrat:wght@400;600&family=Ubuntu:wght@700&display=swap">
<style>
  :root {
    --brand-red: #ec1f27;
    --brand-red-soft: #f04a50;
    --brand-red-deep: #d51b22;
    --light-grey: #dddddd;
    --mid-grey: #919191;
    --ink: #000000;
    --text: #222222;
    --paper: #ffffff;
    --stage: #eeeeee;
  }
  * { box-sizing: border-box; margin: 0; padding: 0; }
  html, body { width: 1200px; height: 863px; overflow: hidden; }
  body {
    background: var(--stage);
    font-family: "Montserrat", Arial, sans-serif;
    display: flex;
    align-items: center;
    justify-content: center;
    gap: 70px;
  }
  .card {
    width: 320px;
    height: 560px;
    position: relative;
    box-shadow: 0 6px 24px rgba(0,0,0,0.12);
  }
  .card--front {
    background: var(--paper);
    display: flex;
    flex-direction: column;
    align-items: center;
  }
  .brand {
    margin-top: 74px;
    display: flex;
    flex-direction: column;
    align-items: center;
  }
  .brand__name {
    font-weight: 600;
    font-size: 22px;
    color: var(--text);
    letter-spacing: 0.3px;
    line-height: 1;
  }
  .brand__tagline {
    margin-top: 7px;
    font-size: 10px;
    color: var(--mid-grey);
    letter-spacing: 0.6px;
  }
  .holder-name {
    margin-top: 72px;
    font-family: "Ubuntu", "Montserrat", sans-serif;
    font-weight: 700;
    font-size: 27px;
    color: var(--brand-red);
  }
  .contact {
    list-style: none;
    margin-top: 44px;
    display: flex;
    flex-direction: column;
    align-items: center;
    gap: 20px;
  }
  .contact__item {
    display: flex;
    flex-direction: column;
    align-items: center;
    gap: 8px;
    font-size: 15px;
    color: var(--text);
  }
  .contact__icon { width: 16px; height: 16px; fill: var(--brand-red); }
  .card__band {
    position: absolute;
    left: 0; right: 0; bottom: 0;
    height: 16px;
    background: var(--brand-red);
  }
  .card--back {
    background: var(--brand-red);
    display: flex;
    align-items: center;
    justify-content: center;
  }
  .back-mark {
    width: 120px;
    height: 120px;
    border-radius: 50%;
    background: var(--brand-red-deep);
  }
</style>
</head>
<body>
  <section class="card card--front" aria-label="Business card front">
    <header class="brand">
      <span class="brand__name">Veltra Systems</span>
      <span class="brand__tagline">IT services for business</span>
    </header>
    <h1 class="holder-name">lorem ipsum</h1>
    <ul class="contact">
      <li class="contact__item">
        <svg class="contact__icon" viewBox="0 0 24 24" aria-hidden="true"><path d="M6.6 10.8a15.1 15.1 0 0 0 6.6 6.6l2.2-2.2a1 1 0 0 1 1-.25 11.4 11.4 0 0 0 3.6.57 1 1 0 0 1 1 1V20a1 1 0 0 1-1 1A17 17 0 0 1 3 4a1 1 0 0 1 1-1h3.5a1 1 0 0 1 1 1c0 1.25.2 2.45.57 3.57a1 1 0 0 1-.25 1z"/></svg>
        <span>+22 33 44 5678</span>
      </li>
      <li class="contact__item">
        <svg class="contact__icon" viewBox="0 0 24 24" aria-hidden="true"><path d="M2 5h20v2l-10 6L2 7z"/><path d="M2 9l10 6 10-6v10H2z"/></svg>
        <span>your_email@domain.com</span>
      </li>
      <li class="contact__item">
        <svg class="contact__icon" viewBox="0 0 24 24" aria-hidden="true"><path d="M12 2a10 10 0 1 0 0 20 10 10 0 0 0 0-20zm6.9 6h-2.9a15 15 0 0 0-1.4-3.6A8 8 0 0 1 18.9 8zM12 4a13 13 0 0 1 1.9 4h-3.8A13 13 0 0 1 12 4zM4.3 14a8 8 0 0 1 0-4h3.4a16 16 0 0 0 0 4zm.8 2h2.9a15 15 0 0 0 1.4 3.6A8 8 0 0 1 5.1 16zM8 8H5.1a8 8 0 0 1 4.3-3.6A15 15 0 0 0 8 8zm4 12a13 13 0 0 1-1.9-4h3.8A13 13 0 0 1 12 20zm2.3-6H9.7a14 14 0 0 1 0-4h4.6a14 14 0 0 1 0 4zm.3 5.6a15 15 0 0 0 1.4-3.6h2.9a8 8 0 0 1-4.3 3.6zM16.3 14a16 16 0 0 0 0-4h3.4a8 8 0 0 1 0 4z"/></svg>
        <span>www.yourwebsite.com</span>
      </li>
    </ul>
    <div class="card__band"></div>
  </section>

  <section class="card card--back" aria-label="Business card back">
    <div class="back-mark" role="img" aria-label="Veltra Systems brand mark"></div>
  </section>
</body>
</html>
```